Homepage for experience sharing site- interesting, fun and personable!

We need a homepage design for an experience sharing website. The tag line is 'find, promote and share great times!' The homepage should be exciting and innovative and illustrate the values of the site: possibility, freedom and life. It should be fun and personable.

To give you a clearer example, here are a few of the 'great times' users will be sharing on the site:

Club night, warehouse rave or beach gig
Antarctic expedition, Cambodian jungle trek
Cooking and surfing classes
Sumo speed dating
Drag racing and quad biking
Birthday parties, pub crawls and comedy nights

We like the idea of some sort of map or background image from which a few experiences pop up; however we are open to other ideas. The links below should give you an idea of the concept.

http://www.marbleco.example/cove#/cove-story
http://www.snaplume.example/map/
http://www.vidorama.example/watch?v=QK7TRW2pLzd
Updates

Hi,

please do not feel that your design must include a map, that was just an idea. If you can produce a design that delivers the message immediately and gets the user interested without a map then that is great! 

Please do not feel constrained.

Thanks,

Marisol

Hi,

I've created and attached two examples to the brief, which I hope will provide some guidance. I want the homepage design to concentrate on the human element and the concept of creating and sharing experiences.

Thanks,

Marisol  

Target Market(s)

18-37 age range. People who enjoy life and new experiences.

Industry/Entity Type

Racing

Requirements
Must have
• It must communicate the human element of the site... please see the attached examples I made as guidance

It must deliver the message as simply as possible

Could you ensure that your design includes the following elements please:

* breadcrumbs
* a search box
* the login and register should be part of the header block
Should not have
• Unnecessary elements

Only yellow

```html
<!DOCTYPE html>
<html lang="en">
<head>
<meta charset="utf-8">
<title>SunnyHours.net – find, share, promote great times</title>
<link rel="stylesheet" href="https://fonts.googleapis.com/css2?family=Arimo:wght@400;700&family=Cinzel:wght@400&family=Crimson+Text:wght@400;700&display=swap">
<style>
:root{
  --sky:#c7f1f7;
  --white:#ffffff;
  --ink:#222222;
  --body:#5a5a5a;
  --green:#9ddc5e;
  --home:#6cbf3c;
  --yellow:#f6c900;
  --blue:#6fc0ee;
  --red:#ee2f3a;
  --strip:#6f7c68;
  --line:#444444;
}
*{margin:0;padding:0;box-sizing:border-box}
html,body{width:1200px;height:609px;overflow:hidden;background:var(--white)}
.page{position:relative;width:1200px;height:609px;overflow:hidden;background:var(--sky);font-family:"Arimo",sans-serif}
.header{position:absolute;left:0;top:0;width:1200px;height:66px;background:var(--white)}
.brand{position:absolute;left:122px;top:17px;font-family:"Crimson Text",serif;font-weight:700;font-size:25px;letter-spacing:.5px;color:var(--ink)}
.tagline{position:absolute;left:378px;top:21px;font-size:17px;color:var(--ink)}
.tagline .find{color:var(--green)}
.tagline .share{color:var(--yellow)}
.tagline .promote{color:var(--blue)}
.tagline .sep{margin:0 6px}
.account{position:absolute;right:126px;top:21px;font-size:17px;color:var(--ink)}
.account .login{color:var(--red)}
.account .register{color:var(--green)}
.world{position:absolute;left:0;top:66px;width:1200px;height:300px;background:radial-gradient(ellipse at 50% 30%,rgba(255,255,255,.35),rgba(255,255,255,0) 70%)}
.breadcrumb{position:absolute;left:134px;top:86px;font-family:"Crimson Text",serif;font-size:19px;color:var(--ink)}
.breadcrumb a{color:var(--home);text-decoration:none}
.site-search{position:absolute;left:781px;top:82px;width:290px;height:32px;background:var(--white);border:1px solid var(--line)}
.site-search span{position:absolute;left:10px;top:3px;font-family:"Crimson Text",serif;font-style:italic;font-size:19px;color:var(--ink)}
.site-search svg{position:absolute;right:8px;top:6px}
.grass{position:absolute;left:0;top:500px;width:1200px;height:55px;z-index:0;background:linear-gradient(rgba(155,205,90,0),rgba(120,180,70,.8))}
.tile{position:absolute;overflow:hidden;z-index:2}
.text-tile{background:var(--white);padding:0 10px 0 14px}
.photo{width:100%;height:100%}
.caption{position:absolute;left:0;bottom:0;width:100%;height:46px;padding:11px 12px 0;font-family:"Cinzel",serif;font-size:19px;line-height:24px;color:var(--white);white-space:nowrap}
.caption.long{font-size:18px;padding-left:11px}
.about h2,.finder h2{font-family:"Crimson Text",serif;font-weight:400;font-size:15px;margin-top:14px}
.about h2{color:var(--green)}
.about p{font-size:12.5px;line-height:17.8px;color:var(--body);margin-top:2px}
.news h2{font-family:"Crimson Text",serif;font-weight:400;font-size:20px;margin-top:10px}
.news .title{display:block;font-size:11.5px;text-decoration:underline;margin-top:4px}
.news .date,.news p{font-size:12.5px;line-height:17.8px;color:var(--body)}
.news .more{display:block;font-size:12.5px;margin-top:1px;text-decoration:none}
.sharing h2,.sharing .title,.sharing .more{color:var(--yellow)}
.promo h2,.promo .title,.promo .more{color:var(--red)}
.finder h2{color:var(--blue)}
.finder p{font-size:12.5px;color:var(--body);margin-top:8px}
.finder .keyword{margin-top:9px;width:229px;height:33px;border:1px solid var(--line);padding:8px;font-size:12px;color:#888}
.finder .go{margin-top:11px;width:98px;height:32px;border-radius:2px;background:linear-gradient(#8ad0f4,#2f93cc);color:var(--white);font-weight:700;font-size:12px;text-align:center;line-height:32px}
.corner{position:absolute;right:-8px;top:0}
.play{position:absolute;left:86px;top:52px}
.strip{position:absolute;left:0;top:553px;width:1200px;height:56px;background:var(--strip);z-index:1}
.thumbs{position:absolute;left:150px;top:563px;display:flex;gap:5.6px;z-index:2}
.thumbs div{width:37.5px;height:37px}
</style>
</head>
<body>
<div class="page">
  <header class="header">
    <div class="brand">SUNNYHOURS.NET</div>
    <div class="tagline"><span class="find">find</span><span class="sep">/</span><span class="share">share</span><span class="sep">/</span><span class="promote">promote</span> &nbsp;great times</div>
    <div class="account"><span class="login">login</span> I <span class="register">register</span></div>
  </header>

  <div class="world" role="img" aria-label="Faint dotted world map behind the content"></div>
  <div class="grass" role="img" aria-label="Tall green grass blades along the bottom"></div>

  <nav class="breadcrumb">You are at <a href="#">Home</a></nav>
  <div class="site-search"><span>search</span>
    <svg width="24" height="20" viewBox="0 0 24 20"><circle cx="9" cy="8" r="6" fill="none" stroke="#333" stroke-width="2"/><line x1="13.5" y1="12" x2="21" y2="18" stroke="#333" stroke-width="3" stroke-linecap="round"/></svg>
  </div>

  <div class="tile" style="left:120px;top:140px;width:236px;height:182px">
    <div class="photo" role="img" aria-label="Video still of friends dancing at a night club" style="background:linear-gradient(135deg,#5a1a12,#c8502a 50%,#e9a070)"></div>
    <svg class="play" width="78" height="78" viewBox="0 0 78 78"><circle cx="39" cy="39" r="38" fill="rgba(120,110,110,.6)"/><polygon points="28,20 62,39 28,58" fill="#1c1c1c"/></svg>
  </div>
  <div class="tile text-tile about" style="left:356px;top:140px;width:234px;height:182px;padding-left:10px">
    <h2>ABOUT SUNNYHOURS.NET</h2>
    <p>Lorem ipsum dolor sit amet, consectetur adipisicing elit, sed do eiusmod tempor incididunt ut labore et dolore magna aliqua. Ut enim ad minim veniam, quis nostrud exercitation ullamco laboris nisi ut aliquip ex ea commodo consequat.</p>
  </div>
  <div class="tile" style="left:590px;top:138px;width:234px;height:184px">
    <div class="photo" role="img" aria-label="Photo of a cooking class with chefs in white hats" style="background:linear-gradient(160deg,#3a3430,#8c7c70 50%,#d8cfc8)"></div>
    <div class="caption" style="background:rgba(150,160,70,.85)">Cooking Classes</div>
  </div>
  <div class="tile text-tile finder" style="left:824px;top:140px;width:257px;height:182px">
    <h2>FIND the GREAT TIMES</h2>
    <p>Find out a lot of great times</p>
    <div class="keyword">keyword</div>
    <div class="go">Search</div>
    <svg class="corner" width="66" height="60" viewBox="0 0 66 60"><polygon points="0,0 66,0 66,60" fill="#2aa6df"/><polygon points="8,0 60,0 60,50" fill="#58c2ef"/></svg>
  </div>

  <div class="tile text-tile news sharing" style="left:120px;top:322px;width:236px;height:179px">
    <h2>Latest Sharing</h2>
    <a class="title" href="#">Sharing Title 1 - Night Club</a>
    <div class="date">15’th May 2011</div>
    <p>Lorem ipsum dolor sit amet, consecte tur adipisicing elit, sed do eiusmod tempor incididunt ut labore et dolore magna aliqua.</p>
    <a class="more" href="#">watch video</a>
  </div>
  <div class="tile" style="left:356px;top:322px;width:234px;height:179px">
    <div class="photo" role="img" aria-label="Photo of a racing driver in a helmet inside his car" style="background:linear-gradient(150deg,#d8d8d8,#7a7a7a 45%,#b02020)"></div>
    <div class="caption" style="background:rgba(170,30,40,.85)">Racing</div>
  </div>
  <div class="tile text-tile news promo" style="left:590px;top:322px;width:234px;height:179px">
    <h2>Latest Promotion</h2>
    <a class="title" href="#">Promo Title 1 - Racing</a>
    <div class="date">15’th May 2011</div>
    <p>Lorem ipsum dolor sit amet, consecte tur adipisicing elit, sed do eiusmod tempor incididunt ut labore et dolore magna aliqua.</p>
    <a class="more" href="#">read more</a>
  </div>
  <div class="tile" style="left:823px;top:322px;width:259px;height:179px">
    <div class="photo" role="img" aria-label="Group photo of an expedition team on a ship deck" style="background:linear-gradient(180deg,#2a7fd0,#4b6c8c 55%,#3a4a4a)"></div>
    <div class="caption long" style="background:rgba(40,80,120,.8)">Antarctic expedition</div>
  </div>

  <div class="strip"></div>
  <div class="thumbs" role="img" aria-label="Row of small photo thumbnails of shared experiences">
    <div style="background:#6a8aa0"></div><div style="background:#4a4a6a"></div><div style="background:#b09070"></div><div style="background:#3a3a4a"></div><div style="background:#5a5030"></div><div style="background:#8a7040"></div><div style="background:#a0b080"></div><div style="background:#505050"></div><div style="background:#d0a030"></div><div style="background:#70a060"></div><div style="background:#303030"></div><div style="background:#8a8a70"></div><div style="background:#c06040"></div><div style="background:#9a5090"></div><div style="background:#8ac8e0"></div><div style="background:#5a9a30"></div><div style="background:#707070"></div><div style="background:#b0c060"></div><div style="background:#404030"></div><div style="background:#6a7040"></div><div style="background:#a0b8c0"></div>
  </div>
</div>
</body>
</html>
```